Bluerock Forge Business Card

We are a US manufacturer of RVM Shotgun Accessories along with some automotive accessories.
Our main business line is definitely the Shotgun Accessories.
Our company is the #1 Leader in RVM upgrade accessories in the United States.
We design, manufacture and retail all our products directly to the end user. We pride ourselves in superior quality and all manufactured in the USA.

On the card I want to convey made in the USA, Superior Quality and being the leader in RVM Accessories.
See our web site for a little information on our company. www.bluerockfw.example

I would like it to have a picture of the RVM shotgun with all our accessories on it like the web site.
The Logo Shield should be a main focus as Branding is important. You can embelish the logo if you wish to make it more "Tactical" or updated looking. Try a few different versions.

Try to use some grey or Aluminum colors in the card. Since we machine metal to make all our products.
I'll send some images you can incorporate into the design.

Thank you.
Dale

Industry/Entity Type

Automotive

Contact Information for Business Card

Bluerock Forge Works Inc.
Dale Prentiss
47 Quarry Lane, Fairbrook, NY 10921
www.BLUEROCKFW.example
1(914)555-0173 (tel)

```html
<!DOCTYPE html>
<html lang="en">
<head>
<meta charset="utf-8">
<title>Bluerock Forge Works Inc. – Business Card</title>
<link href="https://fonts.googleapis.com/css2?family=Arimo:wght@400;700&display=swap" rel="stylesheet">
<style>
  :root {
    --canvas: #e6e4e0;
    --card-white: #ffffff;
    --card-black: #050505;
    --cream: #e3e2cf;
    --ink: #141414;
    --aluminium: #b9bcbf;
    --aluminium-dark: #7d8185;
  }
  * { box-sizing: border-box; margin: 0; padding: 0; }
  html, body { width: 1200px; height: 914px; overflow: hidden; }
  body {
    background: var(--canvas);
    font-family: "Arimo", Arial, sans-serif;
    color: var(--ink);
    display: flex;
    align-items: center;
    justify-content: center;
    gap: 40px;
  }
  .card {
    position: relative;
    width: 560px;
    height: 320px;
    overflow: hidden;
    box-shadow: 0 6px 18px rgba(0,0,0,.22);
  }
  /* Front */
  .card--front { background: var(--card-white); }
  .card__waves { position: absolute; inset: 0; }
  .company-name {
    position: absolute;
    top: 26px;
    right: 28px;
    font-size: 24px;
    font-weight: 400;
    letter-spacing: .2px;
    white-space: nowrap;
  }
  .product-photo {
    position: absolute;
    left: 50px;
    top: 82px;
    width: 200px;
    height: 118px;
    border-radius: 6px;
    background: radial-gradient(ellipse at 40% 45%, #6e7276 0%, #a9adb1 45%, #eceeef 80%, #ffffff 100%);
  }
  .contact {
    position: absolute;
    right: 24px;
    bottom: 26px;
    display: flex;
    gap: 12px;
    align-items: flex-end;
  }
  .contact__lines {
    text-align: right;
    font-size: 13px;
    line-height: 18px;
    white-space: nowrap;
  }
  .contact__icons {
    display: flex;
    flex-direction: column;
    gap: 4px;
    padding-bottom: 2px;
  }
  .contact__icons svg { width: 14px; height: 14px; display: block; }
  /* Back */
  .card--back {
    background: var(--card-black);
    display: flex;
    align-items: center;
    justify-content: center;
    gap: 14px;
  }
  .brand-mark {
    width: 22px;
    height: 22px;
    border-radius: 50%;
    background: var(--aluminium);
  }
  .brand-name {
    font-size: 34px;
    font-weight: 700;
    color: var(--aluminium);
    letter-spacing: 1px;
    white-space: nowrap;
  }
</style>
</head>
<body>

  <section class="card card--front" aria-label="Card front">
    <svg class="card__waves" viewBox="0 0 560 320" aria-hidden="true">
      <path d="M0 258 Q310 262 560 78 L560 320 L0 320 Z" fill="var(--cream)"/>
      <path d="M0 250 Q300 255 520 95 Q545 80 560 70 L560 86 Q320 262 0 258 Z" fill="var(--card-black)"/>
    </svg>
    <h1 class="company-name">Bluerock Forge Works Inc.</h1>
    <div class="product-photo" role="img" aria-label="Photo of machined metal shotgun accessories and tools"></div>
    <div class="contact">
      <div class="contact__lines">
        <p>1(914)555-0173</p>
        <p>www.BLUEROCKFW.example</p>
        <p>Dale Prentiss 47 Quarry Lane,</p>
        <p>Fairbrook, NY 10921</p>
      </div>
      <div class="contact__icons">
        <svg viewBox="0 0 14 14" aria-label="Phone"><path d="M2 5 Q2 2 7 2 Q12 2 12 5 L10 6 L9 4.5 L5 4.5 L4 6 Z M3 7 L11 7 L12 12 L2 12 Z" fill="var(--ink)"/></svg>
        <svg viewBox="0 0 14 14" aria-label="Website"><circle cx="7" cy="7" r="5.5" fill="var(--ink)"/><path d="M1.5 7 H12.5 M7 1.5 Q4 7 7 12.5 Q10 7 7 1.5" stroke="var(--cream)" stroke-width="1" fill="none"/></svg>
        <svg viewBox="0 0 14 14" aria-label="Address"><path d="M7 13 L3 7 A4.5 4.5 0 1 1 11 7 Z" fill="var(--ink)"/><circle cx="7" cy="5" r="1.6" fill="var(--cream)"/></svg>
      </div>
    </div>
  </section>

  <section class="card card--back" aria-label="Card back">
    <span class="brand-mark" aria-hidden="true"></span>
    <span class="brand-name">Bluerock Forge</span>
  </section>

</body>
</html>
```